Buchcover-Design für Coaching-Buch
Zielgruppe
22 Coaches (m/w/d) haben zusammen ein Buch geschrieben - mit ihren besten Tipps, Mut machenden Geschichten und Inspirationen. Herausgekommen ist 'Die stille Mentorin am Fensterbrett - 22 Schatzkisten lüften ihre Rätsel'. Zielgruppe sind vorwiegend Frauen, häufig mit spirituellem Hintergrund oder an Selbstentwicklung interessiert, sowie Menschen, die sich ermutigen lassen möchten und Menschen, die inspirierende Texte und Geschichten mögen. Die Themen sind ganz unterschiedlich, von Selbstliebe über die Wirkung von Farben, vom Überwinden von Krisen und Angst, Umgang mit Emotionen etc. pp. - ein ganzer Blumenstrauß an Themen.
Aufgabenstellung
Der Titel 'Die stille Mentorin am Fensterbrett' kam auf, weil wir die Vorstellung hatten, dass in dem Buch vielleicht abends im Bett gelesen wird und man dann ruhig schlafen kann.
Warum Füllhörner? Nun, jeder Coach hat viel zu geben. Zu jedem Text wird es ein Geschenk geben, das die Autor*innen online zur Verfügung stellen. Dies sind PDFs mit Tipps, Meditationen oder sogar eine kurze Gratis-Session. Es braucht also etwas auf dem Cover, das darauf hindeutet, vielleicht eine Plakette oder etwas Ähnliches, das 'Mit 22 Geschenken' besagt. Im Buchsatz wird dies durch einen Link (E-Book) und durch einen QR-Code (Print) umgesetzt.

```html
<!DOCTYPE html>
<html lang="de">
<head>
<meta charset="utf-8">
<title>Die stille Mentorin am Fensterbrett – Buchcover</title>
<link rel="stylesheet" href="https://fonts.googleapis.com/css2?family=Josefin+Sans:wght@300;400&family=Kaushan+Script&display=swap">
<style>
  :root {
    --page-bg: #ffffff;
    --cover-top: #d6567f;
    --cover-mid: #e65a8c;
    --cover-bottom: #ff6eab;
    --gold: #d8b450;
    --gold-dark: #b58f34;
    --gold-light: #e9cd78;
    --text-light: #fff4f8;
    --fluff-core: #f2c230;
    --fluff-edge: #c98e1c;
  }
  * { margin: 0; padding: 0; box-sizing: border-box; }
  html, body {
    width: 844px; height: 1200px; overflow: hidden;
    background: var(--page-bg);
  }
  .book-cover {
    position: absolute;
    left: 22px; top: 32px;
    width: 800px; height: 1136px;
    background: linear-gradient(180deg, var(--cover-top) 0%, var(--cover-top) 40%, var(--cover-mid) 62%, var(--cover-bottom) 100%);
    box-shadow: 4px 5px 6px rgba(0,0,0,0.35);
    overflow: hidden;
  }
  .title-small {
    position: absolute;
    font-family: "Josefin Sans", sans-serif;
    font-weight: 300;
    font-size: 44px;
    color: var(--text-light);
    letter-spacing: 1px;
    white-space: nowrap;
  }
  .title-small--first { left: 205px; top: 130px; }
  .title-small--second { left: 470px; top: 360px; }
  .title-script {
    position: absolute;
    font-family: "Kaushan Script", cursive;
    color: var(--gold);
    white-space: nowrap;
    line-height: 1;
    text-shadow: 1px 2px 2px rgba(120, 40, 60, 0.25);
  }
  .title-script--main { left: 50px; top: 170px; font-size: 178px; }
  .title-script--place { left: 90px; top: 420px; font-size: 132px; transform: rotate(-3deg); transform-origin: left center; }
  .mascot-photo {
    position: absolute;
    left: 121px; top: 690px;
    width: 362px; height: 310px;
    border-radius: 50% 50% 46% 46%;
    background: radial-gradient(circle at 45% 40%, var(--fluff-core) 0%, #e8aa22 55%, var(--fluff-edge) 100%);
    box-shadow: 30px 30px 40px rgba(170, 40, 90, 0.25);
  }
  .gift-badge {
    position: absolute;
    left: 426px; top: 650px;
    width: 230px; height: 230px;
    border-radius: 50%;
    background: radial-gradient(circle at 35% 30%, var(--gold-light) 0%, var(--gold) 50%, var(--gold-dark) 100%);
    box-shadow: 4px 6px 10px rgba(120, 30, 60, 0.3);
    display: flex; align-items: center; justify-content: center;
    text-align: center;
    transform: rotate(-5deg);
  }
  .gift-badge__text {
    font-family: "Josefin Sans", sans-serif;
    font-weight: 400;
    font-size: 22px;
    line-height: 1.3;
    color: #ffffff;
    text-transform: uppercase;
  }
  .subtitle {
    position: absolute;
    left: 0; right: 0; top: 1058px;
    text-align: center;
    font-family: "Josefin Sans", sans-serif;
    font-weight: 300;
    font-size: 29px;
    color: var(--text-light);
    text-transform: uppercase;
    letter-spacing: 0.5px;
  }
</style>
</head>
<body>
  <main class="book-cover">
    <h1 class="book-title">
      <span class="title-small title-small--first">Die stille</span>
      <span class="title-script title-script--main">Mentorin</span>
      <span class="title-small title-small--second">am</span>
      <span class="title-script title-script--place">Fensterbrett</span>
    </h1>
    <div class="mascot-photo" role="img" aria-label="Foto: flauschiges gelbes Fellknäuel-Wesen auf rosa Hintergrund"></div>
    <div class="gift-badge">
      <p class="gift-badge__text">Inkl.<br>Meditationen,<br>zahlreiche<br>Tipps &amp; Gratis-<br>Session</p>
    </div>
    <p class="subtitle">22 Schatzkisten lüften ihre Rätsel</p>
  </main>
</body>
</html>
```